Australian Trucking Company Requires Professional Looking Stationary

We require a professional looking stationary design that incorporates our newly designed logo.

Our business, called "Vell Haulage Contracting", provides contracting work, transport and logistics to business in Western Australia particularly with links to the mining sector.

We are a small business looking to expand and our new logo and our new stationary will help develop our brand image in our market place.

Target Market(s)

Businesses and Corporation with links to the Mining Sector

Industry/Entity Type

Small Business

Requirements
Must have
• The letterhead must have the following details:
The new logo

Text saying: "Vell Haulage Pty Ltd (ACN 582 306 917) ATF The Vell Discretionary Trust T/AS"
"ABN 71 840 295 613"
Address "P.O Box 718 Norbrook WA, 6043"
Phone: 08 9275 4180
Email: vellhaul@maillane.com.au

The text on the letterhead should be editable as the details are likely to change in the near future. Provision should be made for a website address all though one isn't available at the moment.

The styling, layout and font text is entirely up to the designer.

```html
<!DOCTYPE html>
<html lang="en">
<head>
<meta charset="utf-8">
<title>Vell Haulage Contracting – Business Card</title>
<link rel="stylesheet" href="https://fonts.googleapis.com/css2?family=Titillium+Web:wght@400;600;700&display=swap">
<style>
  :root {
    --backdrop: #d9d9d9;
    --card-white: #ffffff;
    --card-dark: #3a3a3c;
    --card-darker: #2b2b2d;
    --band-grey: #5c5c5f;
    --brand-red: #c8141e;
    --text-grey: #6d6d70;
    --text-light: #f2f2f2;
  }
  * { box-sizing: border-box; margin: 0; padding: 0; }
  html, body {
    width: 1200px;
    height: 900px;
    overflow: hidden;
    background: var(--backdrop);
    font-family: "Titillium Web", Arial, sans-serif;
  }
  .sheet {
    position: relative;
    width: 1200px;
    height: 900px;
  }
  .card {
    position: absolute;
    left: 280px;
    width: 640px;
    height: 366px;
    border-radius: 4px;
    overflow: hidden;
    box-shadow: 0 10px 28px rgba(0,0,0,.25);
  }
  .card--front { top: 60px; background: var(--card-white); }
  .card--back {
    top: 474px;
    background: linear-gradient(160deg, #4a4a4d, var(--card-darker));
    display: flex;
    align-items: center;
    justify-content: center;
    gap: 14px;
  }
  .card__art {
    position: absolute;
    inset: 0;
    width: 100%;
    height: 100%;
  }
  .brand {
    position: absolute;
    left: 42px;
    top: 40px;
    display: flex;
    align-items: flex-start;
    gap: 12px;
  }
  .brand__mark {
    width: 18px;
    height: 18px;
    margin-top: 8px;
    background: var(--brand-red);
  }
  .brand__name {
    color: var(--brand-red);
    font-weight: 700;
    font-size: 30px;
    line-height: 30px;
    text-transform: uppercase;
    letter-spacing: 1px;
  }
  .holder {
    position: absolute;
    right: 42px;
    top: 112px;
    text-align: right;
  }
  .holder__name {
    color: var(--brand-red);
    font-size: 30px;
    font-weight: 600;
    line-height: 32px;
  }
  .holder__role {
    color: var(--text-grey);
    font-size: 17px;
    line-height: 20px;
  }
  .contact {
    position: absolute;
    right: 34px;
    bottom: 18px;
    text-align: right;
    list-style: none;
    color: var(--text-light);
    font-size: 16px;
    line-height: 21px;
  }
  .contact__label { color: var(--brand-red); }
  .card--back .brand__mark--round {
    width: 22px;
    height: 22px;
    border-radius: 50%;
    background: var(--brand-red);
  }
  .card--back .brand__name { font-size: 34px; line-height: 34px; }
</style>
</head>
<body>
<main class="sheet">
  <section class="card card--front" aria-label="Business card front">
    <svg class="card__art" viewBox="0 0 640 366" aria-hidden="true">
      <defs>
        <linearGradient id="baseShade" x1="0" y1="0" x2="1" y2="1">
          <stop offset="0" stop-color="#4a4a4d"/>
          <stop offset="1" stop-color="#262628"/>
        </linearGradient>
      </defs>
      <path d="M0 182 C200 162 380 242 640 214 L640 246 C380 274 200 194 0 214 Z" fill="var(--band-grey)"/>
      <path d="M0 214 C200 194 380 274 640 246 L640 366 L0 366 Z" fill="url(#baseShade)"/>
      <path d="M0 180 C200 160 380 240 640 212" fill="none" stroke="var(--brand-red)" stroke-width="2"/>
      <path d="M0 192 C200 172 380 252 640 224" fill="none" stroke="var(--brand-red)" stroke-width="7"/>
      <path d="M0 204 C200 184 380 264 640 236" fill="none" stroke="#ffffff" stroke-width="1.5" opacity=".8"/>
    </svg>

    <div class="brand">
      <span class="brand__mark"></span>
      <p class="brand__name">Vell Haulage<br>Contracting</p>
    </div>

    <div class="holder">
      <p class="holder__name">YourName</p>
      <p class="holder__role">position</p>
    </div>

    <ul class="contact">
      <li>P.O Box 718 Norbrook WA, 6043</li>
      <li><span class="contact__label">Phone</span>: 08 9275 4180</li>
      <li><span class="contact__label">Email</span>: vellhaul@maillane.com.au</li>
      <li><span class="contact__label">ABN</span>: 71 840 295 613</li>
    </ul>
  </section>

  <section class="card card--back" aria-label="Business card back">
    <span class="brand__mark--round"></span>
    <p class="brand__name">Vell Haulage Contracting</p>
  </section>
</main>
</body>
</html>
```